Poster for List of Company Values

We need a poster to outline our Values which will be displayed in our office as well as posted on our website and other platforms (so need to allow for some flexibly in its application).

File attached outlines what we currently have with design and also our company style guide.

Note that we are looking for a modern, clean look, which still represents our core activities of construction and environmental services.

You can also reference our website here:

https://quorvelgroup.com.au/

Happy to answer any questions you might have.

Thanks for your interest,
Brent

Target Market(s)

Internal and External clients

Industry/Entity Type

Construction, water and recycling

Font styles to use
Sans Serif

Requirements
Must have
• All values on the one page. Graphic to represent each value. Also needs to use company logo
Nice to have
• Preference for poster to be orientated in landscape
Should not have
• Do not follow example provided, this is only to demonstrate what we have to date and also the text required

```html
<!DOCTYPE html>
<html lang="en">
<head>
<meta charset="utf-8">
<title>Quorvel Group – Our Values</title>
<link href="https://fonts.googleapis.com/css2?family=Open+Sans:ital,wght@0,300;0,400;0,700;0,800;1,300;1,400;1,700&display=swap" rel="stylesheet">
<style>
  :root {
    --green: #4faa35;
    --gold: #d3b350;
    --blue: #00368c;
    --orange: #e07a45;
    --red: #c22d46;
    --teal: #45b89c;
    --teal-deep: #43b39b;
    --grey: #c6c6c6;
    --white: #ffffff;
  }
  * { margin: 0; padding: 0; box-sizing: border-box; }
  html, body { width: 1200px; height: 1041px; overflow: hidden; background: var(--white); }
  body { font-family: "Open Sans", Arial, sans-serif; color: var(--white); position: relative; }

  .value-card { position: absolute; overflow: hidden; }
  .card-loyal { left: 0; top: 0; width: 797px; height: 563px; background: var(--green); }
  .card-initiative { left: 811px; top: 0; width: 389px; height: 275px; background: var(--gold); }
  .card-team { left: 811px; top: 289px; width: 389px; height: 275px; background: var(--blue); }
  .card-respect { left: 0; top: 578px; width: 389px; height: 274px; background: var(--orange); }
  .card-open { left: 409px; top: 578px; width: 388px; height: 274px; background: var(--red); }
  .card-positive { left: 811px; top: 578px; width: 389px; height: 274px; background: var(--teal); }

  .brand-name {
    position: absolute; right: 18px; top: 14px;
    font-weight: 700; font-size: 6.5px; line-height: 1; color: var(--white);
    text-transform: uppercase;
  }
  .brand-name span { display: block; text-transform: none; }
  .card-loyal .brand-name { right: 34px; top: 30px; font-size: 13px; }

  .statement { position: absolute; font-size: 11.5px; line-height: 16px; font-weight: 400; }
  .statement em { font-weight: 700; }
  .statement.right { text-align: right; }

  .value-title { position: absolute; line-height: 1; white-space: nowrap; }
  .value-title .verb { font-style: italic; font-weight: 300; }
  .value-title .word { font-weight: 700; }
  .value-title .line { display: block; }

  .pattern { position: absolute; }

  .card-loyal .statement { left: 60px; top: 98px; font-size: 23px; line-height: 32.5px; }
  .card-loyal .value-title { right: 58px; top: 378px; font-size: 92px; }

  .card-initiative .statement { left: 31px; top: 42px; }
  .initiative-word {
    position: absolute; left: 250px; top: 29px; writing-mode: vertical-rl;
    font-weight: 700; font-size: 47px; line-height: 1;
  }
  .initiative-verb {
    position: absolute; left: 294px; top: 80px; writing-mode: vertical-rl;
    font-style: italic; font-weight: 300; font-size: 46px; line-height: 1;
  }

  .card-team .value-title { left: 42px; top: 50px; font-size: 50px; }
  .card-team .statement { right: 17px; top: 188px; }

  .card-respect .statement { left: 30px; top: 72px; }
  .card-respect .value-title { left: 181px; top: 138px; font-size: 49px; }

  .card-open .value-title { left: 29px; top: 52px; font-size: 50px; }
  .card-open .value-title .line + .line { margin-top: -3px; }
  .card-open .statement { left: 30px; top: 169px; font-size: 10.5px; line-height: 14px; }

  .card-positive .value-title { left: 30px; top: 52px; font-size: 50px; }
  .card-positive .statement { right: 20px; top: 168px; }

  .system-row { position: absolute; left: 0; top: 865px; width: 1200px; height: 176px; }
  .system-brand {
    position: absolute; left: 0; top: 0; width: 301px; height: 176px; background: var(--teal-deep);
    display: flex; align-items: center; justify-content: center;
  }
  .system-brand .brand-label { font-weight: 700; font-size: 25px; line-height: 1; text-transform: uppercase; }
  .system-brand .brand-label span { display: block; text-transform: none; }
  .system-cell {
    position: absolute; top: 0; width: 300px; height: 176px;
    border-top: 1.5px solid var(--grey); border-left: 1.5px solid var(--grey);
  }
  .system-cell.one { left: 301px; border-left: none; }
  .system-cell.two { left: 600px; }
  .system-cell.three { left: 900px; }
  .system-cell .source { position: absolute; left: 44px; top: 60px; width: 58px; height: 58px; background: var(--grey); }
  .system-cell .arrow { position: absolute; left: 142px; top: 82px; }
  .system-cell .result { position: absolute; left: 218px; top: 58px; }
</style>
</head>
<body>

<section class="value-card card-loyal">
  <div class="brand-name">Quorvel<span>Group</span></div>
  <p class="statement">We <em>take care</em> of our own and<br>provide opportunities to listen<br>and <em>support</em> each other.</p>
  <svg class="pattern" style="left:0;top:366px" width="122" height="197" viewBox="0 0 122 197" role="img" aria-label="Triangle pattern">
    <polygon points="0,0 0,197 122,197" fill="var(--white)"/>
  </svg>
  <h2 class="value-title"><span class="verb">be</span> <span class="word">LOYAL</span></h2>
</section>

<section class="value-card card-initiative">
  <div class="brand-name">Quorvel<span>Group</span></div>
  <p class="statement">We celebrate and<br>recognize our own and<br>encourage <em>forward<br>thinking</em>.</p>
  <div class="initiative-verb">show</div>
  <div class="initiative-word">INITIATIVE</div>
  <svg class="pattern" style="left:0;top:229px" width="124" height="27" role="img" aria-label="Wave stripe pattern">
    <rect width="124" height="27" rx="6" fill="var(--white)" opacity="0.85"/>
  </svg>
</section>

<section class="value-card card-team">
  <div class="brand-name">Quorvel<span>Group</span></div>
  <h2 class="value-title"><span class="line verb">think</span><span class="line word">TEAM</span></h2>
  <svg class="pattern" style="left:304px;top:83px" width="85" height="28" role="img" aria-label="Slash stripe pattern">
    <rect width="85" height="28" rx="5" fill="var(--white)" opacity="0.85"/>
  </svg>
  <p class="statement right">We <em>communicate</em> effectively and<br>work as a team by helping and<br><em>supporting</em> each other.</p>
</section>

<section class="value-card card-respect">
  <div class="brand-name">Quorvel<span>Group</span></div>
  <p class="statement">We value the <em>diversity</em><br>and opinions of all.</p>
  <svg class="pattern" style="left:0;top:200px" width="99" height="26" role="img" aria-label="Slash stripe pattern">
    <rect width="99" height="26" rx="5" fill="var(--white)" opacity="0.85"/>
  </svg>
  <h2 class="value-title"><span class="line verb">show</span><span class="line word">RESPECT</span></h2>
</section>

<section class="value-card card-open">
  <div class="brand-name">Quorvel<span>Group</span></div>
  <h2 class="value-title"><span class="line"><span class="verb">be</span> <span class="word">OPEN</span></span><span class="line"><span class="verb">and</span> <span class="word">HONEST</span></span></h2>
  <p class="statement">We are clear and open with each other,<br>and provide an approachable and <em>friendly<br>environment</em>.</p>
  <svg class="pattern" style="left:291px;top:226px" width="97" height="27" role="img" aria-label="Wave stripe pattern">
    <rect width="97" height="27" rx="6" fill="var(--white)" opacity="0.85"/>
  </svg>
</section>

<section class="value-card card-positive">
  <div class="brand-name">Quorvel<span>Group</span></div>
  <h2 class="value-title"><span class="line verb">be</span><span class="line word">POSITIVE</span></h2>
  <p class="statement right"><em>SMILE</em><br>We are solutions focused<br>and encourage a <em>positive<br>attitude</em> turning a negative<br>into a positive.</p>
  <svg class="pattern" style="left:0;top:177px" width="60" height="97" viewBox="0 0 60 97" role="img" aria-label="Triangle pattern">
    <polygon points="0,0 0,97 60,97" fill="var(--white)"/>
  </svg>
</section>

<section class="system-row">
  <div class="system-brand"><div class="brand-label">Quorvel<span>Group</span></div></div>

  <div class="system-cell one">
    <div class="source"></div>
    <svg class="arrow" width="34" height="12" viewBox="0 0 34 12"><path d="M0 6H32M27 1l5 5-5 5" stroke="var(--grey)" stroke-width="1.5" fill="none"/></svg>
    <svg class="result" width="37" height="58" viewBox="0 0 37 58" role="img" aria-label="Triangle pattern derived from the brand">
      <polygon points="0,0 0,58 37,58" fill="var(--teal)"/>
    </svg>
  </div>

  <div class="system-cell two">
    <div class="source"></div>
    <svg class="arrow" width="34" height="12" viewBox="0 0 34 12"><path d="M0 6H32M27 1l5 5-5 5" stroke="var(--grey)" stroke-width="1.5" fill="none"/></svg>
    <svg class="result" style="left:200px;top:75px" width="70" height="18" role="img" aria-label="Wave stripe pattern derived from the brand">
      <rect width="70" height="18" rx="5" fill="var(--teal)"/>
    </svg>
  </div>

  <div class="system-cell three">
    <div class="source"></div>
    <svg class="arrow" width="34" height="12" viewBox="0 0 34 12"><path d="M0 6H32M27 1l5 5-5 5" stroke="var(--grey)" stroke-width="1.5" fill="none"/></svg>
    <svg class="result" style="left:193px;top:72px" width="72" height="30" role="img" aria-label="Slash stripe pattern derived from the brand">
      <rect width="72" height="30" rx="5" fill="var(--teal)"/>
    </svg>
  </div>
</section>

</body>
</html>
```